Business Card Design

We need a business card design for a new company called Riverbend Advisory, LLC. We are a project management and software engineering consulting company. We prefer to use blues but am open to any colors. We would like out design to show strength and creativity.

I've uploaded new logo designs to the project.  Please use these logo designs for the business card. Thanks!

Industry/Entity Type

Software

Contact Information for Business Card

Daniel Whitford
Consultant
Owner

Riverbend Advisory, LLC

2716 5th St. S #4372
Arlington, VA 22198

703-555-0187
dwhitford@rvbadv.example
www.rvbadv.example

```html
<!DOCTYPE html>
<html lang="en">
<head>
<meta charset="utf-8">
<title>Riverbend Advisory, LLC — Business Card</title>
<link rel="stylesheet" href="https://fonts.googleapis.com/css2?family=Source+Sans+3:wght@400;700&display=swap">
<style>
  :root {
    --backdrop: #e9eaec;
    --card: #ffffff;
    --navy: #1d3b66;
    --ink: #2b2b2b;
    --muted: #555a61;
    --shadow: rgba(20, 30, 45, 0.18);
  }
  * { box-sizing: border-box; margin: 0; padding: 0; }
  html, body {
    width: 1200px;
    height: 873px;
    overflow: hidden;
    background: var(--backdrop);
    font-family: "Source Sans 3", "Segoe UI", Arial, sans-serif;
  }
  .canvas {
    position: relative;
    width: 1200px;
    height: 873px;
  }
  .card {
    position: absolute;
    top: 288px;
    width: 525px;
    height: 300px;
    background: var(--card);
    box-shadow: 0 6px 18px var(--shadow);
  }
  .card--front { left: 50px; }
  .card--back { left: 625px; }

  .wordmark {
    position: absolute;
    display: flex;
    align-items: center;
    gap: 8px;
    color: var(--navy);
    font-weight: 700;
    text-transform: uppercase;
    letter-spacing: 0.04em;
    line-height: 1;
  }
  .wordmark__square {
    width: 12px;
    height: 12px;
    background: var(--navy);
    flex: none;
  }

  /* Front */
  .card--front .wordmark {
    left: 30px;
    top: 30px;
    font-size: 17px;
  }
  .front-rule {
    position: absolute;
    left: 30px;
    right: 40px;
    height: 1.5px;
    background: var(--navy);
  }
  .front-rule--upper { top: 64px; right: 210px; }
  .front-rule--lower { top: 150px; left: 250px; }
  .identity {
    position: absolute;
    right: 40px;
    top: 96px;
    text-align: right;
  }
  .identity__name {
    font-size: 27px;
    font-weight: 700;
    color: var(--navy);
    line-height: 1;
  }
  .identity__title {
    margin-top: 5px;
    font-size: 13px;
    color: var(--muted);
  }
  .contact {
    position: absolute;
    right: 40px;
    top: 168px;
    text-align: right;
    font-size: 13px;
    line-height: 1.4;
    color: var(--ink);
    list-style: none;
  }
  .contact__gap { margin-top: 10px; }

  /* Back */
  .back-rule {
    position: absolute;
    height: 1.5px;
    background: var(--navy);
  }
  .back-rule--top { top: 28px; left: 60px; right: 28px; }
  .back-rule--bottom { bottom: 28px; left: 185px; right: 28px; }
  .back-url {
    position: absolute;
    left: 28px;
    bottom: 21px;
    font-size: 13px;
    color: var(--muted);
  }
  .card--back .wordmark {
    left: 50%;
    top: 50%;
    transform: translate(-50%, -50%);
    font-size: 24px;
  }
</style>
</head>
<body>
<main class="canvas">
  <section class="card card--front" aria-label="Business card front">
    <div class="wordmark"><span class="wordmark__square"></span>Riverbend Advisory</div>
    <div class="front-rule front-rule--upper"></div>
    <div class="identity">
      <p class="identity__name">Daniel Whitford</p>
      <p class="identity__title">Consultant, Owner Riverbend Advisory</p>
    </div>
    <div class="front-rule front-rule--lower"></div>
    <ul class="contact">
      <li>2716 5th St. S #4372</li>
      <li>Arlington, VA 22198</li>
      <li class="contact__gap">703-555-0187</li>
      <li>dwhitford@rvbadv.example</li>
      <li>www.rvbadv.example</li>
    </ul>
  </section>

  <section class="card card--back" aria-label="Business card back">
    <div class="back-rule back-rule--top"></div>
    <div class="wordmark"><span class="wordmark__square"></span>Riverbend Advisory</div>
    <p class="back-url">www.rvbadv.example</p>
    <div class="back-rule back-rule--bottom"></div>
  </section>
</main>
</body>
</html>
```